DL Flyer for garden consultants. I will supply text and logo

To design an eye catching but simple, uncluttered flyer for letter box distribution. The text and logo are provided.

```html
<!DOCTYPE html>
<html lang="en">
<head>
<meta charset="utf-8">
<title>Fernwood Garden Consultants – DL Flyer</title>
<link href="https://fonts.googleapis.com/css2?family=Bebas+Neue&family=Open+Sans:wght@400;600;700&display=swap" rel="stylesheet">
<style>
  :root {
    --backdrop: #232323;
    --paper: #ffffff;
    --paper-soft: #f1f1f1;
    --lime: #b8cb3c;
    --leaf: #4a8a3a;
    --leaf-text: #3f8a2e;
    --ink: #333326;
    --ring: #555555;
    --grass-light: #dfe8d2;
    --grass-mid: #8fb06a;
    --grass-dark: #2f5a1e;
  }
  * { margin: 0; padding: 0; box-sizing: border-box; }
  html, body { width: 800px; height: 1200px; overflow: hidden; }
  body { background: var(--backdrop); position: relative; font-family: "Open Sans", sans-serif; }

  .flyer { position: absolute; left: 90px; width: 623px; height: 298px; overflow: hidden; background: var(--paper); }
  .flyer--front { top: 192px; }
  .flyer--back { top: 713px; background: linear-gradient(180deg, var(--paper) 0%, var(--paper-soft) 100%); }

  .grass-photo {
    position: absolute; inset: 0;
    background:
      radial-gradient(ellipse at 50% 40%, rgba(255,255,255,0.9) 0%, rgba(255,255,255,0) 55%),
      linear-gradient(180deg, #ffffff 0%, var(--grass-light) 40%, var(--grass-mid) 68%, var(--grass-dark) 100%);
  }

  .brand { position: absolute; left: 34px; top: 30px; display: flex; align-items: center; gap: 12px; }
  .brand__dot { width: 50px; height: 50px; border-radius: 50%; background: var(--leaf); }
  .brand__name { font-family: "Open Sans", sans-serif; font-weight: 600; color: var(--leaf); font-size: 22px; line-height: 1.1; }
  .brand__name span { display: block; font-size: 12px; letter-spacing: 2px; text-transform: uppercase; }

  .headline-band { position: absolute; left: 261px; top: 38px; width: 362px; height: 70px; background: var(--lime); padding: 12px 0 0 24px; font-family: "Bebas Neue", sans-serif; color: var(--ink); }
  .headline-band__small { font-size: 19px; line-height: 1; }
  .headline-band__large { font-size: 35px; line-height: 0.95; }

  .well-band { position: absolute; left: 388px; top: 111px; width: 235px; height: 50px; background: var(--leaf); color: #fff; font-family: "Bebas Neue", sans-serif; font-size: 50px; line-height: 50px; padding-left: 20px; }

  .url { position: absolute; left: 0; right: 0; text-align: center; color: #fff; font-size: 13px; }
  .flyer--front .url { bottom: 12px; }

  .help-band { position: absolute; left: 261px; top: 32px; width: 362px; height: 70px; background: var(--lime); color: #fff; font-family: "Bebas Neue", sans-serif; font-size: 62px; line-height: 74px; padding-left: 30px; }

  .service { position: absolute; width: 180px; text-align: center; color: var(--leaf-text); }
  .service__icon { display: block; margin: 0 auto 10px; }
  .service__title { font-weight: 700; font-size: 11px; line-height: 1.35; }
  .service__note { font-size: 5.5px; color: var(--ink); }
  .service--assess { left: 15px; top: 128px; }
  .service--presale { left: 215px; top: 132px; }
  .service--plants { left: 430px; top: 124px; }
  .service--plants .service__icon { margin-bottom: 14px; }

  .footer-band { position: absolute; left: 0; bottom: 0; width: 100%; height: 38px; background: var(--leaf); }
  .flyer--back .url { bottom: 11px; }
</style>
</head>
<body>

<section class="flyer flyer--front">
  <div class="grass-photo" role="img" aria-label="Photograph of fresh green grass blades against a soft bright bokeh background"></div>
  <div class="brand"><div class="brand__dot"></div><div class="brand__name">Fernwood<span>Garden Consultants</span></div></div>
  <div class="headline-band">
    <div class="headline-band__small">Have you been thinking</div>
    <div class="headline-band__large">About your garden lately?</div>
  </div>
  <div class="well-band">Well...</div>
  <p class="url">www.fernwoodgardens.com.au</p>
</section>

<section class="flyer flyer--back">
  <div class="brand"><div class="brand__dot"></div><div class="brand__name">Fernwood<span>Garden Consultants</span></div></div>
  <div class="help-band">...We can help!</div>

  <div class="service service--assess">
    <svg class="service__icon" width="66" height="66" viewBox="0 0 66 66" aria-hidden="true">
      <circle cx="33" cy="33" r="31.5" fill="none" stroke="var(--ring)" stroke-width="1.2"/>
      <g fill="var(--lime)">
        <circle cx="38" cy="24" r="5"/><circle cx="46" cy="28" r="5"/><circle cx="44" cy="37" r="5"/>
        <circle cx="34" cy="36" r="5"/><circle cx="31" cy="28" r="5"/>
        <circle cx="22" cy="24" r="4"/><circle cx="22" cy="36" r="4"/>
        <path d="M30 40 L36 40 L34 52 L32 52 Z"/>
      </g>
      <circle cx="38.5" cy="30.5" r="3" fill="#fff"/>
    </svg>
    <div class="service__title">Garden Assessment Consultation<br>and Report</div>
    <div class="service__note">...information vital to ensuring your dream becomes reality!</div>
  </div>

  <div class="service service--presale">
    <svg class="service__icon" width="66" height="66" viewBox="0 0 66 66" aria-hidden="true">
      <circle cx="33" cy="33" r="31.5" fill="none" stroke="var(--ring)" stroke-width="1.2"/>
      <g fill="var(--lime)">
        <ellipse cx="21" cy="27" rx="10" ry="6"/><path d="M15 31 L12 37 L20 32 Z"/>
        <ellipse cx="39" cy="35" rx="16" ry="10"/><path d="M45 43 L50 50 L39 44 Z"/>
      </g>
    </svg>
    <div class="service__title">Pre Sale Consultation<br>and Report</div>
    <div class="service__note">...maximise your sale dollar!</div>
  </div>

  <div class="service service--plants">
    <svg class="service__icon" width="70" height="70" viewBox="0 0 70 70" aria-hidden="true">
      <circle cx="35" cy="35" r="33.5" fill="none" stroke="var(--ring)" stroke-width="1.2"/>
      <g fill="var(--lime)">
        <path d="M35 15 C26 15 22 22 22 28 C22 34 28 37 29 43 L41 43 C42 37 48 34 48 28 C48 22 44 15 35 15 Z"/>
        <rect x="29" y="45" width="12" height="3" rx="1"/><rect x="29" y="49" width="12" height="3" rx="1"/>
        <rect x="31" y="53" width="8" height="3" rx="1.5"/>
      </g>
      <path d="M35 41 L35 27 M35 32 C31 30 30 26 31 24 M35 30 C39 28 40 24 39 22" stroke="#fff" stroke-width="1.4" fill="none"/>
    </svg>
    <div class="service__title">Develop &nbsp;a Plant Portfolio</div>
  </div>

  <div class="footer-band"></div>
  <p class="url">www.fernwoodgardens.com.au</p>
</section>

</body>
</html>
```